Display Home Banner PWL

Design a Display Home Banner to go on Fence at Display Home.

Banner will need to display company logo and name.

Prefer the entire banner to be approx 6m in length and approx 1.2m high

Must also have the words "Display Home"

Specialising in unique custom built homes, knock down and rebuild

The rest is up to you to give me some ideas of your own. It needs to be modern and elegant in design. We are show casing our industry leading construction work and want to draw peoples attention to the display home!

**** FURTHER UPDATE ********

Just clarifying that I am looking for a long narrow banner (not poster format)

6 metres long and 1.2 metres high .....

Doesn't have to have construction symbols on it .... can be symbols or shapes or colors or images that compliment the text etc .....

Want the building company logo to be more prominent than the words display home but want it to be clear that its a display home banner ....

I am looking for a slick crisp font .... not too blocky or playful .....

don't want reds, yellows, orange colours ......

looking for tranquil, warm soft colours and colors from the logo ....

I am looking for a very professional corporate banner .....

I will update brief and upload logo and files tonight. Sorry for the delay

Reason: Hi Sorry I have been working on another project with another company and this was left on the side. I have now finished building the display home and need the banner for exhibitions in the coming weeks. The banner needs to display the company logo and name as well as the words "Display Home" I have uploaded the logo files for you to use with your designs. It will be approximately 6m in length and the rest of the design I leave open to your creative side :) Any questions please let me know Thanks

Im not sure that the brief was read correctly by everyone?? I am look for a long narrow banner - 6 metres long and 1.2 metres high ...... (Not Poster format) I want to use peaceful tranquil colors and the colors in our logo ..... (Not Red, Yellow and Orange ..... soft warm colours please) I want a modern striking text like the one in the logo ..... Doesn't necessarily have to have construction symbols in the banner .... can just be shapes or symbols or even just areas defined by colors .... has to look corporate and modern with a professional industry leading look to it ..... Hope this helps ! :) Looking forward to seeing some updated concepts! :) Thanks!

Target Market(s)

People looking for a quality builder to build for them.

Industry/Entity Type

Construction

```html
<!DOCTYPE html>
<html lang="en">
<head>
<meta charset="utf-8">
<title>PWL Display Home Banner</title>
<link rel="stylesheet" href="https://fonts.googleapis.com/css2?family=Open+Sans:wght@600;700&display=swap">
<style>
  :root {
    --navy: #2a2f8f;
    --royal: #2b4fb0;
    --sky: #29a8e0;
    --sky-soft: #4fc3ef;
    --ink: #1c1c1c;
    --paper: #ffffff;
  }
  html, body {
    margin: 0;
    padding: 0;
    width: 1200px;
    height: 533px;
    overflow: hidden;
    background: var(--paper);
  }
  .banner {
    position: relative;
    width: 1200px;
    height: 533px;
    background: var(--paper);
    overflow: hidden;
  }
  .shapes {
    position: absolute;
    inset: 0;
  }
  .brand {
    position: absolute;
    left: 120px;
    top: 150px;
    display: flex;
    align-items: center;
    gap: 26px;
  }
  .brand-square {
    width: 70px;
    height: 70px;
    background: var(--royal);
  }
  .brand-name {
    font-family: "Open Sans", sans-serif;
    font-weight: 600;
    font-size: 150px;
    line-height: 1;
    letter-spacing: 6px;
    color: var(--royal);
  }
  .display-title {
    position: absolute;
    left: 790px;
    top: 196px;
    display: flex;
    align-items: center;
    gap: 16px;
    white-space: nowrap;
  }
  .display-square {
    width: 30px;
    height: 30px;
    background: var(--sky);
  }
  .display-text {
    font-family: "Open Sans", sans-serif;
    font-weight: 600;
    font-size: 50px;
    line-height: 1;
    color: var(--ink);
    text-transform: uppercase;
  }
  .tagline {
    position: absolute;
    left: 0;
    right: 0;
    bottom: 0;
    height: 110px;
    padding: 0 40px;
    display: flex;
    align-items: baseline;
    gap: 20px;
    padding-top: 36px;
    box-sizing: border-box;
    font-family: "Open Sans", sans-serif;
    font-weight: 700;
    color: var(--paper);
    white-space: nowrap;
  }
  .tagline-main {
    font-size: 32px;
  }
  .tagline-extra {
    font-size: 20px;
  }
</style>
</head>
<body>
  <main class="banner">
    <svg class="shapes" width="1200" height="533" viewBox="0 0 1200 533" aria-hidden="true">
      <defs>
        <linearGradient id="band-fill" x1="0" y1="0" x2="1" y2="0">
          <stop offset="0" stop-color="#2a2f8f"/>
          <stop offset="0.55" stop-color="#29a8e0"/>
          <stop offset="0.8" stop-color="#2b4fb0"/>
          <stop offset="1" stop-color="#2a2f8f"/>
        </linearGradient>
        <linearGradient id="wave-fill" x1="0" y1="0" x2="1" y2="0">
          <stop offset="0" stop-color="#29a8e0"/>
          <stop offset="1" stop-color="#4fc3ef"/>
        </linearGradient>
      </defs>
      <path class="wave" d="M700 440 C820 360 1020 330 1200 400 L1200 440 Z" fill="url(#wave-fill)"/>
      <rect class="band" x="0" y="423" width="1200" height="110" fill="url(#band-fill)"/>
    </svg>

    <div class="brand">
      <div class="brand-square"></div>
      <div class="brand-name">PWL</div>
    </div>

    <div class="display-title">
      <div class="display-square"></div>
      <div class="display-text">Display Home</div>
    </div>

    <div class="tagline">
      <span class="tagline-main">Specialising in unique custom built homes,</span>
      <span class="tagline-extra">Knock Down and Rebuild Specialists</span>
    </div>
  </main>
</body>
</html>
```